Tamarack Hearth Partners Business Card

Looking for a new business card layout. We are a real estate firm w/ a logo, old design attached. Must keep the same elements on there, just need a fresh look and possible some foil accents. Looking for a simpler design w/ more modern style.

Target Market(s)

Real Estate clients

Industry/Entity Type

Real Estate Agent

Contact Information for Business Card

see attached

Font styles to use
Sans Serif

Requirements
Must have
• all elements on current biz card
Nice to have
• modern look, simpler than we have!
Should not have
• no serif fonts

```html
<!DOCTYPE html>
<html lang="en">
<head>
<meta charset="utf-8">
<title>Tamarack Hearth Partners – Business Card</title>
<link rel="stylesheet" href="https://fonts.googleapis.com/css2?family=Montserrat:wght@400;500;700&family=Poppins:wght@300;400;500&display=swap">
<style>
  :root {
    --ink: #2f2f2f;
    --signal-red: #ed2128;
    --paper: #ffffff;
    --backdrop: #dedede;
    --photo-light: #e9e2d6;
    --photo-warm: #d8b48f;
    --photo-teal: #4cc3c6;
  }
  * { margin: 0; padding: 0; box-sizing: border-box; }
  html, body { width: 1052px; height: 1200px; overflow: hidden; }
  body { background: var(--backdrop); position: relative; font-family: "Poppins", sans-serif; }

  .card { position: absolute; left: 30px; width: 995px; overflow: hidden; }
  .card-front { top: 26px; height: 566px; background: var(--ink); }
  .card-back { top: 606px; height: 570px; background: var(--paper); }
  .card-shapes { position: absolute; inset: 0; }

  .portrait {
    position: absolute; inset: 0;
    clip-path: polygon(517px 0, 995px 0, 995px 566px, 748px 566px);
    background:
      radial-gradient(ellipse 200px 260px at 760px 260px, var(--photo-warm), transparent 70%),
      radial-gradient(ellipse 260px 140px at 880px 560px, var(--photo-teal), transparent 75%),
      linear-gradient(120deg, var(--photo-light), #cfc6b8);
  }

  .wordmark { position: absolute; color: var(--paper); font-family: "Montserrat", sans-serif; }
  .wordmark-top { display: block; font-weight: 400; letter-spacing: 0.42em; }
  .wordmark-main { display: block; font-weight: 700; line-height: 1; }
  .card-front .wordmark { left: 63px; top: 45px; }
  .card-front .wordmark-top { font-size: 25px; margin-bottom: 6px; padding-left: 3px; }
  .card-front .wordmark-main { font-size: 60px; }

  .name-tag { position: absolute; right: 38px; top: 36px; text-align: right; color: var(--paper); }
  .agent-name { font-family: "Montserrat", sans-serif; font-weight: 500; font-size: 38px; line-height: 1.1; display: block; }
  .agent-role { font-family: "Montserrat", sans-serif; font-weight: 500; font-size: 13px; display: block; margin-top: 6px; }

  .contact-line { position: absolute; left: 98px; color: var(--paper); font-size: 21px; font-weight: 300; line-height: 31px; }
  .contact-phone { top: 300px; }
  .contact-web { top: 382px; }
  .contact-address { top: 463px; }

  .card-back .wordmark { left: 0; right: 0; top: 240px; text-align: center; }
  .card-back .wordmark-top { color: var(--signal-red); font-size: 25px; margin-bottom: 6px; padding-left: 0.42em; }
  .card-back .wordmark-main { color: var(--ink); font-size: 66px; }
</style>
</head>
<body>

<section class="card card-front">
  <div class="portrait" role="img" aria-label="Portrait photograph of the agent"></div>
  <svg class="card-shapes" width="995" height="566" viewBox="0 0 995 566">
    <!-- name tag -->
    <polygon points="697,28 995,28 995,128 722,128" fill="var(--signal-red)"/>
    <rect x="975" y="28" width="20" height="100" fill="var(--ink)"/>
    <!-- address band -->
    <path d="M0,463 H574 L556,528 H0 Z" fill="var(--signal-red)"/>
    <!-- side ticks -->
    <g stroke="var(--paper)" stroke-width="2">
      <line x1="0" y1="331" x2="27" y2="331"/>
      <line x1="0" y1="414" x2="27" y2="414"/>
      <line x1="0" y1="496" x2="27" y2="496"/>
    </g>
    <!-- phone icon -->
    <g transform="translate(62,317)" fill="var(--paper)">
      <path d="M-13,-4 C-13,-10 13,-10 13,-4 L13,0 L7,0 L6,-4 L-6,-4 L-7,0 L-13,0 Z"/>
      <rect x="-9" y="1" width="18" height="10" rx="2"/>
      <g fill="var(--ink)"><circle cx="-4" cy="4" r="1.2"/><circle cx="0" cy="4" r="1.2"/><circle cx="4" cy="4" r="1.2"/><circle cx="-4" cy="8" r="1.2"/><circle cx="0" cy="8" r="1.2"/><circle cx="4" cy="8" r="1.2"/></g>
    </g>
    <!-- globe icon -->
    <g transform="translate(62,414)" fill="none" stroke="var(--paper)" stroke-width="2.4">
      <circle r="12"/>
      <path d="M-12,0 H12 M0,-12 C-7,-6 -7,6 0,12 M0,-12 C7,-6 7,6 0,12"/>
    </g>
    <!-- pin icon -->
    <g transform="translate(62,496)" fill="var(--paper)">
      <path d="M0,14 C-5,7 -10,1 -10,-5 A10,10 0 0 1 10,-5 C10,1 5,7 0,14 Z"/>
      <circle cy="-5" r="3.6" fill="var(--signal-red)"/>
    </g>
  </svg>

  <h1 class="wordmark">
    <span class="wordmark-top">TAMARACK HEARTH</span>
    <span class="wordmark-main">PARTNERS</span>
  </h1>

  <div class="name-tag">
    <span class="agent-name">Marla Venn</span>
    <span class="agent-role">Principle Broker</span>
  </div>

  <p class="contact-line contact-phone">555.210.4816<br>555.317.9052</p>
  <p class="contact-line contact-web">marla@tamarackhearth.com<br>TamarackHearth-Homes.com</p>
  <p class="contact-line contact-address">482 NW Alder Ln<br>Pinecrest, OR 97801</p>
</section>

<section class="card card-back">
  <svg class="card-shapes" width="995" height="570" viewBox="0 0 995 570">
    <path d="M126,0 H876 L830,84 Q822,97 806,97 H196 Q180,97 172,84 Z" fill="var(--signal-red)"/>
    <path d="M0,520 H212 Q228,520 234,534 L250,570 H0 Z" fill="var(--ink)"/>
    <path d="M995,520 H783 Q767,520 761,534 L745,570 H995 Z" fill="var(--ink)"/>
    <path d="M226,570 L264,493 Q271,480 286,480 H716 Q731,480 738,493 L777,570 Z" fill="var(--signal-red)"/>
  </svg>
  <h2 class="wordmark">
    <span class="wordmark-top">TAMARACK HEARTH</span>
    <span class="wordmark-main">PARTNERS</span>
  </h2>
</section>

</body>
</html>
```